WATTLE HILL PRIMARY SCHOOL - WHPS STATIONARY and Promo Pack

Stationary Design

We are a Western Australian Independent Public Primary School called Wattle Hill Primary School.

We are looking for a new fresh and modern stationary design that reflects our innovative open minded approach.

The school colours are in the teak, turquoise range, basically ocean colours as the school is literally 3 minutes away from the beach and has ocean views.

Feel free to incorporate the school motto: Be Your Best
Feel also free to incorporate our values: Respect, Resilience, Cooperation, Responsibility, Tolerance and Excellence

LIST of DELIVERABLES:

#1: Brand identity elements:
• business card

• stationary - basic package including

o letterhead (print ready)
o envelope design
 DL 110 x 220
 DLX 120 x 235
 A4 229 x 324 and (all print ready)
o template for invoices (delivered as PDF file and Word file)
o cover page for annual report (digital file)
o Notepad A4

• PowerPoint template (delivered as PP file)

• Social media banners & logo avatars (delivered as digital files. Facebook, twitter, pinterest, instagram, google plus)

• With compliment slip (DL size - 210mmx 99mm)

• Thank you card (A6)

• A2 poster background (420mm x 594mm)

#2: Brand promotion elements:

• Staff -T - shirt design - long sleeve and short sleeve polo - (Delivered as mock up and digital file / vector)

• Sport banner (roughly 1800mm x 3000) – needs to be in a darker colour please

• Featherbanner (196 x600mm) compare sketch

Industry/Entity Type

School

Contact Information for Business Card

compare provided sample - all info on that one needs to be used please

Colors
85abd2
0355a3
85acd3
eaf1f7
00a990
33b8a4
87cfc6
cfeae6
cee9f5

Requirements
Must have
• LIST of DELIVERABLES:
• #1: Brand identity elements:
• • business card
• • stationary - basic package including
• o letterhead (print ready)
• o envelope design
•  DL 110 x 220
•  DLX 120 x 235
•  A4 229 x 324 and (all print ready)
• o template for invoices (delivered as PDF file and Word file)
• o cover page for annual report (digital file)
• o Notepad A4
• • PowerPoint template (delivered as PP file)
• • Social media banners & logo avatars (delivered as digital files. Facebook, twitter, pinterest, instagram, google plus)
• • With compliment slip (DL size - 210mmx 99mm)
• • Thank you card (A6)
• • A2 poster background (420mm x 594mm)
• #2: Brand promotion elements:
• • Staff -T - shirt design - long sleeve and short sleeve polo - (Delivered as mock up and digital file / vector)
• • Sport banner (roughly 1800mm x 3000) – needs to be in a darker colour please
• • Featherbanner (196 x600mm) compare sketch

```html
<!DOCTYPE html>
<html lang="en">
<head>
<meta charset="utf-8">
<title>Wattle Hill Primary School – DL Envelope</title>
<link rel="stylesheet" href="https://fonts.googleapis.com/css2?family=Cabin:ital,wght@0,500;1,400;1,500&display=swap">
<style>
  :root {
    --flap: #2f8f98;
    --band-dark: #20757b;
    --ink: #1e5f74;
    --paper: #ffffff;
    --outline: #3a3a3a;
    --wash-light: #eef7f7;
    --wash-mint: #d6ece8;
  }
  html, body {
    margin: 0;
    padding: 0;
    overflow: hidden;
    background: var(--paper);
  }
  .canvas {
    width: 1197px;
    height: 1200px;
    position: relative;
    overflow: hidden;
  }
  .envelope {
    display: block;
    width: 1197px;
    height: 1200px;
  }
  .school-name {
    font-family: "Cabin", sans-serif;
    font-style: italic;
    font-weight: 500;
    font-size: 24px;
    fill: var(--ink);
  }
  .school-details {
    font-family: "Cabin", sans-serif;
    font-style: italic;
    font-weight: 400;
    font-size: 15px;
    fill: var(--ink);
  }
  .emblem-name {
    font-family: "Cabin", sans-serif;
    font-weight: 500;
    font-size: 19px;
    letter-spacing: 2px;
    fill: var(--ink);
  }
</style>
</head>
<body>
<div class="canvas">
  <svg class="envelope" viewBox="0 0 1055 1059" preserveAspectRatio="none" xmlns="http://www.w3.org/2000/svg">
    <defs>
      <radialGradient id="wash-fill" cx="0.6" cy="0.6" r="0.7">
        <stop offset="0" stop-color="var(--wash-mint)"/>
        <stop offset="0.6" stop-color="var(--wash-light)"/>
        <stop offset="1" stop-color="var(--paper)"/>
      </radialGradient>
    </defs>

    <!-- flaps -->
    <polygon class="flap-top" points="140,0 890,0 995,104 45,104" fill="var(--flap)"/>
    <polygon class="flap-left" points="0,138 45,104 45,580 0,540" fill="var(--flap)"/>
    <polygon class="flap-right" points="995,104 1055,140 1055,540 995,580" fill="var(--flap)"/>

    <!-- front panel -->
    <rect class="front-panel" x="45" y="104" width="950" height="476" fill="var(--paper)"/>

    <!-- header swoosh bands -->
    <path class="band-dark" d="M45,104 H995 V118 C800,150 500,160 45,152 Z" fill="var(--band-dark)"/>
    <path class="band-sweep" d="M45,166 C400,205 700,215 995,178 V143 C750,185 450,195 45,166 Z" fill="var(--band-dark)"/>

    <!-- decorative illustration area -->
    <rect class="illustration-area" role="img" aria-label="Soft ocean wave illustration"
          x="720" y="225" width="275" height="355" fill="url(#wash-fill)"/>

    <!-- fold line -->
    <line class="fold-line" x1="45" y1="580" x2="995" y2="580" stroke="#555" stroke-width="1.2" stroke-dasharray="8 5"/>
    <line class="side-guide" x1="45" y1="104" x2="45" y2="580" stroke="#888" stroke-width="1" stroke-dasharray="6 5"/>
    <line class="side-guide" x1="995" y1="104" x2="995" y2="580" stroke="#888" stroke-width="1" stroke-dasharray="6 5"/>

    <!-- pocket -->
    <rect class="pocket" x="45" y="580" width="950" height="475" fill="var(--paper)" stroke="var(--outline)" stroke-width="1.4"/>

    <!-- emblem -->
    <circle class="emblem-mark" cx="190" cy="320" r="46" fill="var(--ink)"/>
    <text class="emblem-name" x="190" y="392" text-anchor="middle">WHPS</text>

    <!-- return address -->
    <text class="school-name" x="85" y="432">Wattle Hill Primary School</text>
    <text class="school-details" x="85" y="455">An Independent Public School</text>
    <text class="school-details" x="85" y="474">Wattle Hill Road, Coral Bay, WA 6999</text>
    <text class="school-details" x="85" y="493">Telephone: (08) 9500 1234</text>
    <text class="school-details" x="85" y="512">Facsimile: (08) 9500 1299</text>
    <text class="school-details" x="85" y="532">ABN 12 345 678 901</text>
  </svg>
</div>
</body>
</html>
```